Vex

I have the logo for the back already. Need the front to match.
Need a VEX logo which I can provide or you can download one - VEX Realty in canada... Back of the card will be my logo and name. Front will have the info...
I would like a black background. Match colors on front to the back..
Details on Card

Target Market(s)

Realestate clients.. Keep it classy like the logo

Contact Information for Business Card

Moren Tadwick office - 5817730264 cell - 5819063147 email - Moren@MorenTadwick.Com. website - MorenTadwick.Com Facebook - MTadwRealty Instagram - Moren_Qpl_Realtor Address - 418 - 23 St NE | K5P2M8

Colors
3176b5
33a6d7
85cae6

Requirements
Must have
• same color scheme as the logo
logo will be on the back
Black Background
Horizontal card
The one side of the card should be clean. like I stated, just my logo " Moren Tadwick " and nothing else

```html
<!DOCTYPE html>
<html lang="en">
<head>
<meta charset="utf-8">
<title>Moren Tadwick – Business Card</title>
<link href="https://fonts.googleapis.com/css2?family=PT+Sans:wght@400;700&display=swap" rel="stylesheet">
<style>
  :root {
    --page: #ffffff;
    --card-centre: #4b4b4d;
    --card-edge: #323234;
    --strip: #3a3a3c;
    --blue: #2176c2;
    --white: #ffffff;
    --text-font: "PT Sans", sans-serif;
  }
  * { margin: 0; padding: 0; box-sizing: border-box; }
  html, body {
    width: 1028px; height: 1200px; overflow: hidden;
    background: var(--page);
    font-family: var(--text-font);
  }
  .sheet { position: relative; width: 1028px; height: 1200px; }

  .card {
    position: absolute;
    background: radial-gradient(ellipse at 50% 50%, var(--card-centre) 0%, var(--card-edge) 75%);
    color: var(--white);
  }
  .card--front { left: 35px; top: 35px; width: 856px; height: 547px; }
  .card--back  { left: 35px; top: 618px; width: 959px; height: 547px; }

  .edge-strip {
    position: absolute; left: 960px; top: 35px; width: 34px; height: 547px;
    background: var(--strip);
  }

  .identity { position: absolute; left: 136px; top: 110px; }
  .identity__name { font-size: 45px; line-height: 1; font-weight: 400; }
  .identity__first { color: var(--blue); }
  .identity__title { font-size: 34px; line-height: 1; margin-top: 14px; }
  .identity__title sup { font-size: 16px; vertical-align: 16px; }

  .affiliations {
    position: absolute; left: 34px; top: 362px;
    display: flex; align-items: center; gap: 28px;
  }
  .badge-shape {
    width: 96px; height: 84px;
    border: 2px solid rgba(255,255,255,0.85);
    border-radius: 4px;
  }
  .badge-shape--wide { width: 112px; height: 60px; }
  .brokerage {
    display: flex; align-items: center; gap: 8px;
    font-size: 28px; font-weight: 700; color: var(--white); white-space: nowrap;
  }
  .brokerage__mark {
    width: 16px; height: 16px; border-radius: 50%; background: var(--white);
  }

  .contacts {
    position: absolute; right: 2px; top: 100px;
    list-style: none; text-align: right;
  }
  .contacts li {
    font-size: 31px; line-height: 51.2px; letter-spacing: 0.3px;
    white-space: nowrap;
  }

  .contact-icons {
    position: absolute; left: 906px; top: 119px;
    display: flex; flex-direction: column; gap: 15.2px;
  }
  .contact-icons svg { width: 38px; height: 36px; display: block; }

  .back-name {
    position: absolute; left: 0; right: 0; top: 240px;
    text-align: center;
    font-size: 72px; font-weight: 700; letter-spacing: 4px;
    color: var(--blue);
  }
</style>
</head>
<body>
<div class="sheet">

  <section class="card card--front">
    <div class="identity">
      <h1 class="identity__name"><span class="identity__first">Moren</span> Tadwick</h1>
      <p class="identity__title">Realtor<sup>®</sup></p>
    </div>

    <div class="affiliations">
      <div class="badge-shape" role="img" aria-label="Partner network badge"></div>
      <div class="brokerage"><span class="brokerage__mark"></span>VEX Realty</div>
      <div class="badge-shape badge-shape--wide" role="img" aria-label="Luxury listing network badge"></div>
    </div>

    <ul class="contacts">
      <li>5817730264</li>
      <li>5819063147</li>
      <li>Moren@MorenTadwick.Com</li>
      <li>MorenTadwick.Com</li>
      <li>MTadwRealty</li>
      <li>Moren_Qpl_Realtor</li>
      <li>418 - 23 St NE | K5P2M8</li>
    </ul>
  </section>

  <div class="contact-icons" aria-hidden="true">
    <!-- office phone -->
    <svg viewBox="0 0 38 36"><path fill="var(--blue)" d="M9 3c1.5-.8 3-.5 3.8 1l3 5.5c.7 1.3.3 2.8-.9 3.6l-2.2 1.5c1.6 3.8 4.7 7 8.6 8.7l1.6-2.1c.9-1.2 2.4-1.5 3.6-.8l5.4 3.1c1.4.8 1.7 2.4.9 3.8l-1.5 2.5c-1.2 2-3.6 2.9-5.8 2.2C17.7 30 8.6 21 5.6 11.3 4.9 9 5.9 6.6 7.9 5.4z"/></svg>
    <!-- mobile -->
    <svg viewBox="0 0 38 36"><rect x="11" y="1.5" width="16" height="33" rx="3" fill="none" stroke="var(--blue)" stroke-width="3"/><line x1="16" y1="29" x2="22" y2="29" stroke="var(--blue)" stroke-width="2.5"/></svg>
    <!-- mail -->
    <svg viewBox="0 0 38 36"><rect x="2" y="7" width="34" height="22" fill="none" stroke="var(--blue)" stroke-width="3"/><path d="M2 7l17 13L36 7M2 29l13-11M36 29L23 18" fill="none" stroke="var(--blue)" stroke-width="2.5"/></svg>
    <!-- web -->
    <svg viewBox="0 0 38 36"><g fill="none" stroke="var(--blue)" stroke-width="2.4"><circle cx="19" cy="18" r="16"/><ellipse cx="19" cy="18" rx="7" ry="16"/><line x1="19" y1="2" x2="19" y2="34"/><line x1="3" y1="18" x2="35" y2="18"/><path d="M6 10h26M6 26h26"/></g></svg>
    <!-- social page -->
    <svg viewBox="0 0 38 36"><circle cx="19" cy="18" r="13" fill="none" stroke="var(--blue)" stroke-width="3"/></svg>
    <!-- photo profile -->
    <svg viewBox="0 0 38 36"><rect x="4" y="3" width="30" height="30" rx="6" fill="none" stroke="var(--blue)" stroke-width="3"/></svg>
    <!-- location pin -->
    <svg viewBox="0 0 38 36"><path fill="var(--blue)" fill-rule="evenodd" d="M19 1c7 0 12 5 12 11.5C31 21 19 35 19 35S7 21 7 12.5C7 6 12 1 19 1zm0 6.5a5 5 0 1 0 0 10 5 5 0 0 0 0-10z"/></svg>
  </div>

  <div class="edge-strip"></div>

  <section class="card card--back">
    <h2 class="back-name">MOREN TADWICK</h2>
  </section>

</div>
</body>
</html>
```